Lotus Reed Kitchen Road Billboard

Road Billboard I need all of this information on it
Authentic Thai Food Bangkok Style
6.5 Miles on the right
4172 Marlow Rd Pelham NC
828-555-0147

```html
<!DOCTYPE html>
<html lang="en">
<head>
<meta charset="utf-8">
<title>Lotus Reed Kitchen Road Billboard</title>
<link rel="stylesheet" href="https://fonts.googleapis.com/css2?family=Bebas+Neue&family=Fondamento&display=swap">
<style>
  :root {
    --page-bg: #e6e6e6;
    --board-black: #000000;
    --gold: #d9a821;
    --white: #ffffff;
  }
  html, body {
    margin: 0;
    padding: 0;
    width: 1200px;
    height: 817px;
    overflow: hidden;
    background: var(--page-bg);
  }
  .canvas {
    position: relative;
    width: 1200px;
    height: 817px;
  }
  .billboard {
    position: absolute;
    left: 40px;
    top: 252px;
    width: 1120px;
    height: 313px;
    background: var(--board-black);
    color: var(--white);
    font-family: "Bebas Neue", "Oswald", sans-serif;
  }
  .brand {
    position: absolute;
    left: 18px;
    top: 30px;
    display: flex;
    align-items: center;
    gap: 28px;
  }
  .brand-mark {
    width: 150px;
    height: 150px;
    flex: 0 0 auto;
  }
  .brand-name {
    margin: 0;
    font-family: "Fondamento", serif;
    font-weight: 400;
    font-size: 104px;
    line-height: 1;
    color: var(--gold);
    white-space: nowrap;
  }
  .info-row {
    position: absolute;
    left: 18px;
    top: 186px;
    display: flex;
    align-items: stretch;
    height: 96px;
  }
  .info-block {
    display: flex;
    flex-direction: column;
    justify-content: space-between;
    line-height: 1;
    white-space: nowrap;
  }
  .info-block .small {
    font-size: 42px;
    letter-spacing: 0.5px;
  }
  .info-block .large {
    font-size: 70px;
    margin-bottom: -6px;
  }
  .divider {
    width: 5px;
    background: var(--white);
    margin: 4px 10px 0;
  }
  .gold { color: var(--gold); }
  .white { color: var(--white); }
  .direction-arrow {
    width: 104px;
    height: 96px;
    margin-left: 8px;
  }
</style>
</head>
<body>
<div class="canvas">
  <section class="billboard">
    <header class="brand">
      <svg class="brand-mark" viewBox="0 0 150 150" aria-hidden="true">
        <circle cx="75" cy="75" r="60" fill="var(--gold)"/>
      </svg>
      <h1 class="brand-name">Lotus Reed Kitchen</h1>
    </header>

    <div class="info-row">
      <div class="info-block contact">
        <span class="small white">4172 Marlow Rd Pelham NC</span>
        <span class="large gold">828-555-0147</span>
      </div>
      <div class="divider"></div>
      <div class="info-block tagline">
        <span class="small gold">Authentic Thai Food</span>
        <span class="large white">Bangkok Style</span>
      </div>
      <div class="divider"></div>
      <div class="info-block directions">
        <span class="small white">6.5 Miles On</span>
        <span class="large gold">The Right</span>
      </div>
      <svg class="direction-arrow" viewBox="0 0 104 96" aria-label="Arrow pointing right">
        <polygon points="0,2 32,2 74,48 32,94 0,94 42,48" fill="var(--white)"/>
        <polygon points="30,12 44,12 80,48 44,84 30,84 66,48" fill="var(--gold)"/>
        <polygon points="58,12 70,12 104,48 70,84 58,84 92,48" fill="var(--white)"/>
      </svg>
    </div>
  </section>
</div>
</body>
</html>
```